Letterhead creation for military law attorney

I need letterhead design for my business. We are now only doing military law and need to change address, logo and vision. I like the idea of using an eagle or a jolly roger flag

Target Market(s)

Military Law Clients

Colors
3176b5
85abd2

Requirements
Must have
• We are defending people against the government
Nice to have
• Jolly Roger Flag

```html
<!DOCTYPE html>
<html lang="en">
<head>
<meta charset="utf-8">
<title>Harlan Defense Letterhead</title>
<link href="https://fonts.googleapis.com/css2?family=Open+Sans:wght@400;700&display=swap" rel="stylesheet">
<style>
  :root {
    --navy: #1b2d4f;
    --red: #d3324f;
    --ink-grey: #7a7f88;
    --mark-grey: #eeeeee;
    --backdrop: #d9dcdf;
    --paper: #ffffff;
  }
  * { box-sizing: border-box; margin: 0; padding: 0; }
  html, body {
    width: 1200px; height: 784px; overflow: hidden;
    background: var(--backdrop);
    font-family: "Open Sans", Arial, sans-serif;
  }
  .letterhead {
    position: absolute; left: 314px; top: 22px;
    width: 572px; height: 740px;
    background: var(--paper);
    box-shadow: 0 2px 10px rgba(0,0,0,0.12);
    overflow: hidden;
  }
  .header-tab {
    position: absolute; left: 0; top: 30px;
    width: 26px; height: 5px; background: var(--navy);
  }
  .brand {
    position: absolute; left: 38px; top: 22px;
    display: flex; align-items: center; gap: 8px;
  }
  .brand-dot {
    width: 14px; height: 14px; border-radius: 50%; background: var(--navy);
  }
  .brand-name {
    font-size: 13px; font-weight: 400; letter-spacing: 0.5px; color: var(--navy);
  }
  .header-rule {
    position: absolute; left: 232px; right: 0; top: 30px;
    height: 5px; background: var(--red);
  }
  .flag-mark {
    position: absolute; left: 170px; top: 250px;
    width: 240px; height: 190px;
    background: var(--mark-grey);
    border-radius: 6px;
    transform: rotate(-8deg);
  }
  .footer-address {
    position: absolute; left: 34px; top: 630px;
    font-size: 11px; font-weight: 700; color: var(--navy);
  }
  .footer-contacts {
    position: absolute; left: 34px; top: 652px;
    display: flex; gap: 12px; align-items: center;
    font-size: 9px; color: var(--ink-grey);
  }
  .contact-item { display: flex; align-items: center; gap: 4px; }
  .contact-icon { width: 10px; height: 10px; }
  .footer-stripes {
    position: absolute; left: 0; bottom: 0; width: 572px; height: 60px;
  }
  .footer-web {
    position: absolute; right: 0; bottom: 0;
    width: 190px; height: 30px;
    background: var(--navy);
    color: #fff; font-size: 11px; font-weight: 700;
    display: flex; align-items: center; justify-content: center;
  }
</style>
</head>
<body>
  <main class="letterhead">
    <div class="header-tab"></div>
    <div class="brand">
      <span class="brand-dot"></span>
      <span class="brand-name">HARLAN DEFENSE, PLLC</span>
    </div>
    <div class="header-rule"></div>

    <div class="flag-mark" role="img" aria-label="Faint pirate flag watermark"></div>

    <p class="footer-address">4820 Ridgeline Pkwy, Cedar Bluff, KY 40999, USA</p>
    <div class="footer-contacts">
      <span class="contact-item">
        <svg class="contact-icon" viewBox="0 0 10 10"><circle cx="5" cy="5" r="5" fill="var(--red)"/><path d="M5 2.2a1.8 1.8 0 0 1 1.8 1.8C6.8 5.4 5 7.8 5 7.8S3.2 5.4 3.2 4A1.8 1.8 0 0 1 5 2.2z" fill="#fff"/></svg>
        PO Box 218 Millbrook, TN 37000
      </span>
      <span class="contact-item">
        <svg class="contact-icon" viewBox="0 0 10 10"><circle cx="5" cy="5" r="5" fill="var(--red)"/><path d="M3.2 2.6l1 1-0.5 0.8a3 3 0 0 0 1.9 1.9l0.8-0.5 1 1-0.7 0.8C4.8 7.4 2.6 5.2 2.4 3.3z" fill="#fff"/></svg>
        555 014 2270
      </span>
      <span class="contact-item">
        <svg class="contact-icon" viewBox="0 0 10 10"><circle cx="5" cy="5" r="5" fill="var(--red)"/><rect x="2.6" y="3" width="4.8" height="4" fill="#fff"/></svg>
        555 014 2271
      </span>
      <span class="contact-item">
        <svg class="contact-icon" viewBox="0 0 10 10"><circle cx="5" cy="5" r="5" fill="var(--red)"/><rect x="2.4" y="3.2" width="5.2" height="3.6" fill="#fff"/><path d="M2.4 3.2L5 5.2 7.6 3.2" stroke="var(--red)" stroke-width="0.6" fill="none"/></svg>
        contact@harlandefense.com
      </span>
    </div>

    <svg class="footer-stripes" viewBox="0 0 572 60" aria-hidden="true">
      <polygon points="0,18 120,18 126,24 0,24" fill="var(--red)"/>
      <polygon points="130,18 250,18 256,24 136,24" fill="var(--navy)"/>
      <polygon points="260,18 372,18 378,24 266,24" fill="var(--red)"/>
      <polygon points="0,30 372,30 382,40 382,60 0,60" fill="var(--navy)"/>
      <rect x="0" y="42" width="372" height="3" fill="var(--paper)"/>
    </svg>
    <div class="footer-web">www.harlandefense.com</div>
  </main>
</body>
</html>
```